Business Card Design Project

We need a buisness card for a new digital sinage company. Our target cliants are small to mediaum buisness who want to advertise on out digital sinage network

Target Market(s)

Small to medium buisness

Industry/Entity Type

Digital

Requirements
Must have
• Must have logo

```html
<!DOCTYPE html>
<html lang="en">
<head>
<meta charset="utf-8">
<title>Glowcast Business Card</title>
<link rel="stylesheet" href="https://fonts.googleapis.com/css2?family=Ubuntu:wght@400;700&display=swap">
<style>
  :root {
    --page-bg: #d9d9d9;
    --card-bg: #fbfbf9;
    --brand-blue: #1c66b0;
    --brand-green: #4f9526;
    --brand-orange: #f0a117;
    --ink: #161616;
    --shadow: rgba(0, 0, 0, 0.18);
  }
  html, body {
    margin: 0;
    padding: 0;
    width: 1200px;
    height: 1200px;
    overflow: hidden;
    background: var(--page-bg);
    font-family: "Ubuntu", sans-serif;
  }
  .canvas {
    position: relative;
    width: 1200px;
    height: 1200px;
  }
  .card {
    position: absolute;
    left: 190px;
    width: 820px;
    height: 469px;
    background: var(--card-bg);
    box-shadow: 0 10px 30px var(--shadow);
    overflow: hidden;
  }
  .card--front { top: 100px; }
  .card--back { top: 630px; }

  /* Front side */
  .front-mark {
    position: absolute;
    left: 90px;
    top: 150px;
    width: 170px;
    height: 170px;
    background: var(--brand-blue);
  }
  .contact-block {
    position: absolute;
    left: 380px;
    top: 105px;
  }
  .person-name {
    margin: 0;
    font-weight: 700;
    font-size: 50px;
    letter-spacing: 2px;
    color: var(--brand-blue);
    line-height: 1;
  }
  .person-role {
    margin: 4px 0 36px;
    font-size: 24px;
    color: var(--brand-blue);
  }
  .contact-list {
    list-style: none;
    margin: 0;
    padding: 0;
  }
  .contact-item {
    display: flex;
    align-items: center;
    gap: 16px;
    font-size: 21px;
    letter-spacing: 1px;
    margin-bottom: 22px;
    color: var(--brand-green);
  }
  .contact-item svg { width: 20px; height: 20px; flex: none; }
  .contact-item--web { color: var(--brand-orange); }

  /* Back side */
  .brand-lockup {
    position: absolute;
    left: 0;
    right: 0;
    top: 0;
    bottom: 0;
    display: flex;
    align-items: center;
    justify-content: center;
    gap: 28px;
  }
  .brand-square {
    width: 90px;
    height: 90px;
    background: var(--brand-blue);
  }
  .brand-name {
    font-weight: 700;
    font-size: 96px;
    color: var(--ink);
    letter-spacing: -2px;
  }
</style>
</head>
<body>
<main class="canvas">
  <section class="card card--front" aria-label="Business card front">
    <div class="front-mark"></div>
    <div class="contact-block">
      <h1 class="person-name">JOHN DOE</h1>
      <p class="person-role">CEO</p>
      <ul class="contact-list">
        <li class="contact-item">
          <svg viewBox="0 0 20 20" aria-hidden="true"><path d="M10 2 L19 10 H16 V18 H12 V13 H8 V18 H4 V10 H1 Z" fill="currentColor"/></svg>
          Your Address
        </li>
        <li class="contact-item">
          <svg viewBox="0 0 20 20" aria-hidden="true"><rect x="5" y="1" width="10" height="18" rx="2" fill="none" stroke="currentColor" stroke-width="2"/><circle cx="10" cy="15.5" r="1.2" fill="currentColor"/></svg>
          0123 45 00 789
        </li>
        <li class="contact-item">
          <svg viewBox="0 0 20 20" aria-hidden="true"><rect x="1" y="4" width="18" height="12" fill="currentColor"/><path d="M1 4 L10 11 L19 4" fill="none" stroke="#fbfbf9" stroke-width="1.6"/></svg>
          johndoe@brightpanel.com
        </li>
        <li class="contact-item contact-item--web">
          <svg viewBox="0 0 20 20" aria-hidden="true"><circle cx="10" cy="10" r="8.5" fill="none" stroke="currentColor" stroke-width="2"/><path d="M1.5 10 H18.5 M10 1.5 C6 6 6 14 10 18.5 M10 1.5 C14 6 14 14 10 18.5" fill="none" stroke="currentColor" stroke-width="1.4"/></svg>
          www.brightpanel.com
        </li>
      </ul>
    </div>
  </section>

  <section class="card card--back" aria-label="Business card back">
    <div class="brand-lockup">
      <div class="brand-square"></div>
      <span class="brand-name">Glowcast</span>
    </div>
  </section>
</main>
</body>
</html>
```